Wine bottle labels - front and back - art and text provided

I have a logo (ai file) with our artwork, as well as all necessary text. I just need someone to put it all together and make it look neat, professional, and stylish, like a regular commercial wine bottle should be. This will be used for the front and back labels for our wine bottles for our very small home vineyard, not commercial use. I would like the style to be similar to the Copper Fern Tulare Basin brand with simple colors (grey and silver), and transparent so they can be screen-printed. I need both ai and jpg files. Note: There need to be two versions of each label. One with the date on the front and the ALC percentage on the back to see the complete look. The second version, without these items. This is because we are having all bottles screen printed without this information since we have a very small production, and will be adding small stickers WITH the information during bottling so that we can use the same bottles for years to come. Art file is attached. Front label text in addition to art: Cabernet Sauvignon 55% / Merlot 45% 2018 California. The back label should read: MARBLEWOOD ESTATE Nestled in the heart of the “Amber Crescent” in Cedar Bluffs, CA, the vineyard at Marblewood Estate enjoys a year-round growing season. Nourished by the fertile black clay soil, the vineyard is surrounded by lush French lavender, fragrant roses, numerous fruit trees, and grazing horses. The Hartwell family has been tending the vineyard at Marblewood Estate since 2014. Our blend of 55% Cabernet Sauvignon and 45% Merlot results in a wine that is deep, vibrant, complex, and full of life. Enjoy our wine responsibly. Salut! Produced and bottled by Marblewood Estate, Alder Springs, Oregon. GOVERNMENT WARNING: (1) ACCORDING TO THE SURGEON GENERAL, WOMEN SHOULD NOT DRINK ALCOHOLIC BEVERAGES DURING PREGNANCY BECAUSE OF THE RISK OF BIRTH DEFECTS. (2) CONSUMPTION OF ALCOHOLIC BEVERAGES IMPAIRS YOUR ABILITY TO DRIVE A CAR OR OPERATE MACHINERY, AND MAY CAUSE HEALTH PROBLEMS. CONTAINS SULFITES / 13.9% ALC BY VOL / 750 ML ***Font can be no smaller than 2mm tall, and items in bold must be the entire Government Warning and the "55% Cabernet Sauvignon / 45% Merlot".

Font styles to use
Serif
Script

Colors
cbcbcb

Requirements
Must have
• Transparent image in grey and silver so that the black bottle will show through the image as a background color.
Nice to have
• It would be nice to see the outline of the artwork in silver and everything else in grey. (see sample file of "Copper Fern" below.)

```html
<!DOCTYPE html>
<html lang="en">
<head>
<meta charset="utf-8">
<title>Marblewood Estate – Wine Labels</title>
<link href="https://fonts.googleapis.com/css2?family=Tinos:ital,wght@0,400;0,700;1,400;1,700&display=swap" rel="stylesheet">
<style>
  :root {
    --paper: #ffffff;
    --ink: #8c8c8c;
    --ink-strong: #828282;
    --frame: #9a9a9a;
  }
  * { margin: 0; padding: 0; box-sizing: border-box; }
  html, body {
    width: 1038px; height: 1200px; overflow: hidden;
    background: var(--paper);
  }
  .sheet {
    position: absolute; left: 6px; top: 0;
    width: 1300px; height: 1520px;
    transform: scale(0.7895); transform-origin: 0 0;
    font-family: "Tinos", "Times New Roman", serif;
    color: var(--ink);
  }
  .label-set { position: absolute; left: 0; width: 1300px; height: 720px; }
  .label-set--dated { top: 0; }
  .label-set--blank { top: 757px; }

  .frame { position: absolute; left: 0; top: 0; overflow: visible; }
  .frame path { fill: none; stroke: var(--frame); stroke-width: 6; }

  /* Front label */
  .front-name {
    position: absolute; left: 28px; width: 600px; top: 300px;
    text-align: center; color: var(--ink); font-weight: 400;
  }
  .front-name__main { display: block; font-size: 66px; letter-spacing: 3px; line-height: 1; }
  .front-name__sub { display: block; font-size: 28px; letter-spacing: 10px; margin-top: 14px; line-height: 1; }
  .varietals {
    position: absolute; left: 26px; width: 600px; top: 486px;
    text-align: center; font-style: italic; font-weight: 700;
    font-size: 28px; line-height: 37px; color: var(--ink);
  }
  .vintage {
    position: absolute; left: 26px; width: 600px; top: 594px;
    text-align: center; font-weight: 700; font-size: 24px; letter-spacing: 1px;
  }

  /* Back label */
  .back-title {
    position: absolute; left: 672px; width: 530px; top: 52px;
    text-align: center; font-weight: 700; font-size: 22px; letter-spacing: 1.2px;
  }
  .back-story {
    position: absolute; left: 706px; width: 536px; top: 89px;
    font-style: italic; font-size: 20.5px; line-height: 27px; letter-spacing: 1.1px;
    text-align: justify; text-align-last: center;
  }
  .back-story strong { font-weight: 700; color: var(--ink-strong); }
  .back-line {
    position: absolute; left: 706px; width: 536px;
    text-align: center; font-style: italic; font-size: 20.5px; line-height: 27px; letter-spacing: 1.1px;
  }
  .back-line--toast { top: 368px; }
  .back-line--producer { top: 405px; }
  .warning {
    position: absolute; left: 706px; width: 536px; top: 481px;
    font-weight: 700; font-size: 16px; line-height: 25px; letter-spacing: 1.5px;
    text-transform: uppercase; color: var(--ink-strong);
  }
  .warning__title { text-align: center; }
  .warning__body { text-align: justify; text-align-last: center; }
  .warning__facts { text-align: center; }
  .warning__blank { display: inline-block; width: 44px; }
</style>
</head>
<body>
<main class="sheet">

  <section class="label-set label-set--dated">
    <svg class="frame" width="1300" height="720" viewBox="0 0 1300 720" aria-hidden="true">
      <path d="M70,158 L115,158 Q135,158 135,138 L135,110 Q135,62 185,62 L475,62 Q525,62 525,110 L525,138 Q525,158 545,158 L588,158 A40,40 0 0 0 628,198 L628,420 A40,40 0 0 0 588,460 L70,460 A40,40 0 0 0 28,420 L28,198 A40,40 0 0 0 70,158 Z"/>
      <path d="M742,30 L1208,30 A58,58 0 0 0 1272,88 L1272,650 A58,58 0 0 0 1208,712 L742,712 A58,58 0 0 0 676,650 L676,88 A58,58 0 0 0 742,30 Z"/>
    </svg>
    <div class="front-name">
      <span class="front-name__main">MARBLEWOOD</span>
      <span class="front-name__sub">ESTATE</span>
    </div>
    <p class="varietals">Cabernet Sauvignon 55%<br>Merlot 45%</p>
    <p class="vintage">2018</p>

    <h2 class="back-title">MARBLEWOOD ESTATE</h2>
    <p class="back-story">Nestled in the heart of the “Amber Crescent” in Cedar Bluffs, CA, the vineyard at Marblewood Estate enjoys a year-round growing season. Nourished by the fertile black clay soil, the vineyard is surrounded by lush French lavender, fragrant roses, numerous fruit trees, and grazing horses. The Hartwell family has been tending the vineyard at Marblewood Estate since 2014. Our blend of <strong>55% Cabernet Sauvignon and 45% Merlot</strong> results in a wine that is deep, vibrant, complex, and full of life.</p>
    <p class="back-line back-line--toast">Enjoy our wine responsibly. SALUT!</p>
    <p class="back-line back-line--producer">Produced and bottled by<br>Marblewood Estate, Alder Springs, Oregon.</p>
    <div class="warning">
      <p class="warning__title">Government Warning:</p>
      <p class="warning__body">(1) According to the Surgeon General, women should not drink alcoholic beverages during pregnancy because of the risk of birth defects.</p>
      <p class="warning__body">(2) Consumption of alcoholic beverages impairs your ability to drive a car or operate machinery, and may cause health problems</p>
      <p class="warning__facts">Contains sulfites / 13.9% alc by vol / 750 ml.</p>
    </div>
  </section>

  <section class="label-set label-set--blank">
    <svg class="frame" width="1300" height="720" viewBox="0 0 1300 720" aria-hidden="true">
      <path d="M70,158 L115,158 Q135,158 135,138 L135,110 Q135,62 185,62 L475,62 Q525,62 525,110 L525,138 Q525,158 545,158 L588,158 A40,40 0 0 0 628,198 L628,420 A40,40 0 0 0 588,460 L70,460 A40,40 0 0 0 28,420 L28,198 A40,40 0 0 0 70,158 Z"/>
      <path d="M742,30 L1208,30 A58,58 0 0 0 1272,88 L1272,650 A58,58 0 0 0 1208,712 L742,712 A58,58 0 0 0 676,650 L676,88 A58,58 0 0 0 742,30 Z"/>
    </svg>
    <div class="front-name">
      <span class="front-name__main">MARBLEWOOD</span>
      <span class="front-name__sub">ESTATE</span>
    </div>
    <p class="varietals">Cabernet Sauvignon 55%<br>Merlot 45%</p>

    <h2 class="back-title">MARBLEWOOD ESTATE</h2>
    <p class="back-story">Nestled in the heart of the “Amber Crescent” in Cedar Bluffs, CA, the vineyard at Marblewood Estate enjoys a year-round growing season. Nourished by the fertile black clay soil, the vineyard is surrounded by lush French lavender, fragrant roses, numerous fruit trees, and grazing horses. The Hartwell family has been tending the vineyard at Marblewood Estate since 2014. Our blend of <strong>55% Cabernet Sauvignon and 45% Merlot</strong> results in a wine that is deep, vibrant, complex, and full of life.</p>
    <p class="back-line back-line--toast">Enjoy our wine responsibly. SALUT!</p>
    <p class="back-line back-line--producer">Produced and bottled by<br>Marblewood Estate, Alder Springs, Oregon.</p>
    <div class="warning">
      <p class="warning__title">Government Warning:</p>
      <p class="warning__body">(1) According to the Surgeon General, women should not drink alcoholic beverages during pregnancy because of the risk of birth defects.</p>
      <p class="warning__body">(2) Consumption of alcoholic beverages impairs your ability to drive a car or operate machinery, and may cause health problems</p>
      <p class="warning__facts">Contains sulfites / <span class="warning__blank"></span>% alc by vol / 750 ml.</p>
    </div>
  </section>

</main>
</body>
</html>
```